omitted Email Design for Weekly New Products Email

We would like to send a weekly email to our customers highlighting four of the new jewelry pieces we have for sale each week. The email should be professionally looking, and have the same look and feel of our website, calvinmarlowgems.com. The template would have our logo on the top or left header, and would then have a block of text which would stay the same each week. This block would say "This weeks new arrivals won't last long, shop now with discount code "EMAIL10" to receive 10% off your entire purchase!"
Then below that, there would space for four images, which I will need to change every week. Below each image, there should be room for a title description of the image, which I will need to change each week. An example title would be "18k Yellow Gold Curb Necklace"
Then below the found images, maybe a black action button that says "SHOP NOW". Also, each of the images should be clickable links, which I can edit to add the link to the specific item.
I have attached a few images so you can use them for the mockup. Also, if there are any other ideas you have to make it look better please do!
Thanks,
Ned
It only allowed me to upload one image, so I uploaded the EPS file of our logo. You can use the product images from our website, calvinmarlowgems.com for the product images for now.

```html
<!DOCTYPE html>
<html lang="en">
<head>
<meta charset="utf-8">
<title>Calvin Marlow Jewelers – Weekly New Arrivals</title>
<link href="https://fonts.googleapis.com/css2?family=Arimo:wght@400;700&display=swap" rel="stylesheet">
<style>
  :root {
    --page: #f4f4f4;
    --panel: #f2f2f2;
    --header: #ffffff;
    --ink: #1f1f1f;
    --muted: #333333;
    --gold: #d09b26;
    --black: #111111;
    --footer: #222222;
    --rule: #bdbdbd;
    --soft-rule: #e2e2e2;
    --white: #ffffff;
  }
  * { box-sizing: border-box; margin: 0; padding: 0; }
  html, body { width: 1200px; height: 1200px; overflow: hidden; background: var(--page); }
  body { font-family: "Arimo", Arial, sans-serif; color: var(--ink); }

  .email {
    position: absolute; left: 327px; top: 17px;
    width: 546px; height: 1166px;
    background: var(--panel);
    box-shadow: 0 0 30px rgba(0,0,0,0.12);
  }

  .brand-header {
    height: 54px; background: var(--header);
    display: flex; align-items: center; justify-content: center;
  }
  .brand-name {
    font-family: "Arimo", Arial, sans-serif; font-weight: 400;
    font-size: 18px; color: var(--ink); line-height: 1;
  }

  .hero-bar { height: 9px; background: var(--black); }
  .hero-photo {
    height: 256px;
    background: linear-gradient(135deg, #2a2b31 0%, #4a4844 50%, #25262c 100%);
  }

  .intro {
    height: 86px; margin: 0 16px;
    border-bottom: 1px solid var(--rule);
    text-align: center; padding-top: 7px;
  }
  .intro p { line-height: 1.1; color: var(--ink); }
  .intro .lead { font-size: 21px; }
  .intro .mid { font-size: 16.5px; margin-top: 1px; }
  .intro .close { font-size: 21.5px; margin-top: 2px; }
  .highlight { color: var(--gold); }

  .products { margin: 25px 16px 0; }
  .product-row {
    height: 300px; display: flex; justify-content: space-between;
    border-bottom: 1px solid var(--soft-rule);
  }
  .product-row + .product-row { margin-top: 25px; }
  .product {
    width: 242px; display: flex; flex-direction: column; align-items: center;
    text-decoration: none; color: var(--ink);
  }
  .product-photo { width: 242px; height: 191px; border: 1px solid #dcdcdc; }
  .photo-necklace { background: linear-gradient(180deg, #f6f6f4 0%, #ece4cf 100%); }
  .photo-earrings { background: linear-gradient(180deg, #eef0f1 0%, #e2e5ea 100%); }
  .photo-ring { background: linear-gradient(180deg, #ffffff 0%, #f3f1ec 100%); }
  .photo-chain { background: linear-gradient(180deg, #f6f6f4 0%, #ebe3d2 100%); }
  .product-title {
    margin-top: 15px; font-size: 12.8px; line-height: 19px;
    text-align: center; color: var(--muted); height: 38px;
  }
  .shop-now {
    margin-top: 18px; background: var(--black); color: var(--white);
    font-size: 12.5px; line-height: 15px; padding: 0 4px;
  }

  .site-footer {
    position: absolute; left: 0; bottom: 0; width: 546px; height: 94px;
    background: var(--footer); color: var(--white);
    display: flex; flex-direction: column; align-items: center;
  }
  .social { display: flex; gap: 26px; margin-top: 20px; }
  .social svg { display: block; }
  .copyright { margin-top: 27px; font-size: 10.5px; }
  .copyright a { color: var(--white); text-decoration: underline; }
</style>
</head>
<body>
  <main class="email">
    <header class="brand-header">
      <div class="brand-name">Calvin Marlow Jewelers</div>
    </header>

    <div class="hero-bar"></div>
    <div class="hero-photo" role="img" aria-label="Silver estate jewelry arranged on a dark background: watch, chains, bracelet and rings"></div>

    <section class="intro">
      <p class="lead">This week's new arrivals won't last long,</p>
      <p class="mid">shop now with discount code &nbsp;<span class="highlight">"EMAIL10"</span>&nbsp; to</p>
      <p class="close">receive <span class="highlight">10% off</span> your entire purchase!</p>
    </section>

    <section class="products">
      <div class="product-row">
        <a class="product" href="#">
          <div class="product-photo photo-necklace" role="img" aria-label="Yellow gold mesh wheat necklace on a white bust"></div>
          <p class="product-title">18k Yellow Gold Diamond Emerald Fancy<br>Mesh Wheat Necklace 17.5"</p>
          <span class="shop-now">SHOP NOW</span>
        </a>
        <a class="product" href="#">
          <div class="product-photo photo-earrings" role="img" aria-label="Pair of oval blue lapis stud earrings"></div>
          <p class="product-title">18k Yellow Gold Diamond Emerald Fancy<br>Mesh Wheat Necklace 17.5"</p>
          <span class="shop-now">SHOP NOW</span>
        </a>
      </div>
      <div class="product-row">
        <a class="product" href="#">
          <div class="product-photo photo-ring" role="img" aria-label="Gold ring with black onyx and mother of pearl inlay"></div>
          <p class="product-title">14k Yellow Gold Black Onyx and Mother of<br>Pearl Inlay Ring Size 7</p>
          <span class="shop-now">SHOP NOW</span>
        </a>
        <a class="product" href="#">
          <div class="product-photo photo-chain" role="img" aria-label="Yellow gold braided wheat chain necklace on a white bust"></div>
          <p class="product-title">14k Yellow Gold 35.2g Soft Braided Wheat<br>Chain Necklace Italy 17 Inches</p>
          <span class="shop-now">SHOP NOW</span>
        </a>
      </div>
    </section>

    <footer class="site-footer">
      <nav class="social" aria-label="Social links">
        <svg width="22" height="22" viewBox="0 0 22 22" aria-label="Social profile"><circle cx="11" cy="11" r="10" fill="none" stroke="#ffffff" stroke-width="1.3"/></svg>
        <svg width="22" height="22" viewBox="0 0 22 22" aria-label="Website"><circle cx="11" cy="11" r="10" fill="none" stroke="#ffffff" stroke-width="1.3"/><path d="M9.5 12.5l3-3M8.8 11.2l-1.3 1.3a1.8 1.8 0 0 0 2.5 2.5l1.3-1.3M13.2 10.8l1.3-1.3a1.8 1.8 0 0 0-2.5-2.5l-1.3 1.3" fill="none" stroke="#ffffff" stroke-width="1.2" stroke-linecap="round"/></svg>
        <svg width="22" height="22" viewBox="0 0 22 22" aria-label="Social profile"><circle cx="11" cy="11" r="10" fill="none" stroke="#ffffff" stroke-width="1.3"/></svg>
      </nav>
      <p class="copyright">© 2020 <a href="#">Calvin Marlow Jewelers</a></p>
    </footer>
  </main>
</body>
</html>
```